Update shopping site

Our current shopping website is outdated and we are wanting to update our shopping site to have a fresh new look/design.

Create a Web Design (Uncoded - PSD layout only)

We want you to develop the design for 4 pages:
1) Home Page
2) Remedy Type
3) Health Condition
4) Consultations

www.fernmoorwell.com

Reason: Close to choosing design and a few missing items to be resolved.

Industry/Entity Type

Shopping

```html
<!DOCTYPE html>
<html lang="en">
<head>
<meta charset="utf-8">
<title>Fernmoor Well – Botanical Health Care</title>
<link href="https://fonts.googleapis.com/css2?family=Josefin+Sans:wght@300;400&display=swap" rel="stylesheet">
<style>
  :root{
    --forest:#02623f;
    --leaf:#2fa05a;
    --mint:#8cc79a;
    --ink:#1b241e;
    --white:#ffffff;
    --header-veil:rgba(240,242,236,0.82);
  }
  *{margin:0;padding:0;box-sizing:border-box;}
  html,body{width:936px;height:1200px;overflow:hidden;}
  body{position:relative;font-family:'Josefin Sans',sans-serif;font-weight:300;color:var(--ink);background:#fff;}

  .hero{position:absolute;left:0;top:0;width:936px;height:625px;
    background:
      linear-gradient(rgba(230,232,220,0.35),rgba(230,232,220,0.35)),
      radial-gradient(circle at 12% 40%,#b8744f 0,transparent 22%),
      radial-gradient(circle at 30% 18%,#b7ae7a 0,transparent 20%),
      radial-gradient(circle at 55% 25%,#9da47a 0,transparent 22%),
      radial-gradient(circle at 80% 18%,#a8695f 0,transparent 20%),
      radial-gradient(circle at 22% 78%,#d2c35a 0,transparent 20%),
      radial-gradient(circle at 65% 78%,#c98a4c 0,transparent 20%),
      radial-gradient(circle at 88% 78%,#e4e2da 0,transparent 16%),
      radial-gradient(circle at 85% 48%,#8f7a8f 0,transparent 20%),
      #a79d80;}

  .site-header{position:absolute;left:0;top:0;width:936px;height:82px;background:var(--header-veil);}
  .brand{position:absolute;left:85px;top:7px;width:70px;height:70px;border-radius:50%;
    background:var(--white);border:1.5px solid #8a9a8c;display:flex;align-items:center;justify-content:center;
    text-align:center;font-size:12px;line-height:13px;color:var(--forest);font-weight:400;}
  .main-nav{position:absolute;top:33px;left:0;display:flex;font-size:17px;}
  .main-nav a{position:absolute;white-space:nowrap;text-decoration:none;color:var(--ink);}
  .main-nav a.active{color:var(--leaf);}

  .headline{position:absolute;left:0;width:936px;text-align:center;text-transform:uppercase;font-weight:300;}
  .headline .line{position:absolute;left:0;width:936px;letter-spacing:9px;font-size:38px;white-space:nowrap;}
  .headline .big{color:var(--white);font-size:56px;letter-spacing:10px;}

  .slider-dots{position:absolute;top:551px;left:403px;display:flex;gap:8px;}
  .slider-dots span{width:38px;height:3px;background:#3a3a32;}
  .slider-dots span.current{background:#6fcf7e;}

  .intro-band{position:absolute;left:0;top:625px;width:936px;height:205px;background:var(--forest);}
  .section-title{position:absolute;top:118px;width:936px;text-align:center;color:var(--white);font-size:38px;letter-spacing:8px;}
  .section-kicker{position:absolute;top:163px;left:227px;width:482px;display:flex;align-items:center;gap:8px;
    color:var(--mint);font-size:17px;letter-spacing:4px;}
  .section-kicker::before,.section-kicker::after{content:"";flex:1;height:1px;background:#0f2a1e;}

  .about{position:absolute;left:0;top:830px;width:936px;height:370px;
    background:linear-gradient(180deg,#7f8d79 0%,#93a08c 45%,#a4ad9c 100%);}
  .about-text{position:absolute;top:40px;left:68px;width:800px;text-align:center;color:var(--white);
    text-transform:uppercase;font-size:17px;letter-spacing:3.6px;line-height:33px;font-weight:400;}
</style>
</head>
<body>
  <section class="hero" role="img" aria-label="Sacks of dried herbs, spices and flower petals in warm earthy colours"></section>

  <header class="site-header">
    <div class="brand">Fernmoor<br>Well</div>
    <nav class="main-nav">
      <a class="active" href="#" style="left:213px">HOME</a>
      <a href="#" style="left:293px">ABOUT US</a>
      <a href="#" style="left:401px">REMEDY TYPE</a>
      <a href="#" style="left:537px">HEALTH CONDITION</a>
      <a href="#" style="left:723px">CONSULTATIONS</a>
    </nav>
  </header>

  <h1 class="headline">
    <span class="line" style="top:186px">Imagine the best &nbsp;botanical</span>
    <span class="line" style="top:258px">health care products</span>
    <span class="line" style="top:318px"><span class="big">Now</span> &nbsp;imagine</span>
    <span class="line" style="top:390px">something <span class="big">better</span></span>
  </h1>

  <div class="slider-dots"><span class="current"></span><span></span><span></span></div>

  <svg style="position:absolute;left:0;top:560px" width="936" height="70" aria-hidden="true">
    <polygon points="410,66 468,9 526,66" fill="var(--forest)"/>
    <polyline points="452,43 468,57 484,43" fill="none" stroke="#111" stroke-width="4.5"/>
  </svg>

  <section class="intro-band">
    <h2 class="section-title">WHO WE ARE?</h2>
    <div class="section-kicker">ABOUT US</div>
  </section>

  <section class="about" role="img" aria-label="Glass bottles holding fresh herb sprigs on a wooden table">
    <p class="about-text">We offer some of the best botanical health care products in our industry (we require certificate of analysis from our suppliers to ensure the purity of our product, that it is free of pesticides, contaminants, mold, fungus and it is the right product); we have over 300 NPN (natural product number) licenses approved by Health Northland and our friendly staff is well qualified to answer most questions you may have. &nbsp;We also partner with professional practitioners if you require a more thorough consultation</p>
  </section>

  <svg style="position:absolute;left:450px;top:829px" width="36" height="14" aria-hidden="true">
    <polygon points="0,0 36,0 18,14" fill="var(--forest)"/>
  </svg>
</body>
</html>
```